Home Design company focused on remodel and enhancement of kitchens and bathroorms

I already have a logo designed by ArtHarbor, I now need a design for my business cards.
The company is in the remodeling and enhancement industry for homes, focusing on kitchens and bathrooms, however, we can remodel or enhance every room in a home, an office space, etc.

The company's name is VELMOR HOME DESIGN, LLC

We'll focus on clients in the Rio Grande Valley, Texas. Primarily McAllen, Edinburg, Pharr, Mission, Brownsville and South Padre Island.

The design on the business card should transmit reliability, professionalism anda bit of upscale design.

The logo is in black and white, and would like to keep it that way.

The information that needs to be printed in the business cards is:
Company's name: Velmor Home Design
Company's Logo (attached)
My name: Noel Bramwit
Address, phone and email:
2715 N Parkline Road, Ste 348
Larkdale, TX 79999
(555) 555 0187
nbramwit@velmordesign.example
Website: velmordesign.example

```html
<!DOCTYPE html>
<html lang="en">
<head>
<meta charset="utf-8">
<title>Velmor Home Design — Business Card</title>
<link rel="stylesheet" href="https://fonts.googleapis.com/css2?family=Cabin:wght@500;600&family=Montserrat:wght@400&family=Open+Sans:wght@600&display=swap">
<style>
  :root {
    --page: #ffffff;
    --ink: #111111;
    --black: #000000;
    --arc-1: #e0dfe0;
    --arc-2: #efefef;
    --arc-3: #f7f7f7;
    --arc-light: #d9d8d9;
    --arc-mid: #959595;
    --ghost: #efeeef;
    --name: #e2e2e2;
    --contact: #ffffff;
    --rule: #8a8a8a;
    --rule-thin: #4a4a4a;
  }
  * { box-sizing: border-box; margin: 0; padding: 0; }
  html, body {
    width: 1027px; height: 1200px; overflow: hidden;
    background: var(--page);
  }
  .sheet { position: relative; width: 1027px; height: 1200px; }
  .card {
    position: absolute; left: 91px; width: 844px; height: 482px;
    overflow: hidden; background: var(--page);
    box-shadow: 0 0 18px rgba(0,0,0,0.28);
  }
  .card--front { top: 75px; }
  .card--back { top: 618px; }
  .card__bg { position: absolute; inset: 0; width: 844px; height: 482px; }

  .ghost-name {
    position: absolute;
    font-family: "Montserrat", sans-serif; font-weight: 400;
    color: var(--ghost); font-size: 122px; letter-spacing: 6px;
    line-height: 1; white-space: nowrap;
  }
  .card--front .ghost-name { left: 543px; top: 402px; }
  .card--back .ghost-name { left: 6px; top: 378px; }

  .wordmark {
    position: absolute;
    font-family: "Montserrat", sans-serif;
    font-weight: 400; color: var(--ink);
    text-transform: uppercase; line-height: 1.02;
  }
  .wordmark span { display: block; }
  .card--front .wordmark {
    left: 190px; top: 200px; width: 470px;
    font-size: 34px; letter-spacing: 14px; text-align: center;
  }
  .card--back .wordmark {
    left: 57px; top: 211px; width: 285px;
    font-size: 20px; letter-spacing: 8px; text-align: center;
  }

  .contact { position: absolute; left: 466px; top: 0; width: 378px; height: 482px; }
  .contact__name {
    position: absolute; left: 2px; top: 100px;
    font-family: "Open Sans", sans-serif; font-weight: 600;
    font-size: 31px; letter-spacing: -1px; color: var(--name);
    text-transform: uppercase; white-space: nowrap;
  }
  .contact__rule { position: absolute; height: 2px; background: var(--rule); }
  .contact__rule--name { left: 87px; right: 0; top: 158px; }
  .contact__line {
    position: absolute; left: 0;
    font-family: "Cabin", sans-serif; font-weight: 600;
    font-size: 20px; line-height: 1; color: var(--contact); white-space: nowrap;
  }
  .contact__divider { position: absolute; left: 0; height: 1px; background: var(--rule-thin); }
</style>
</head>
<body>
<main class="sheet">

  <section class="card card--front" aria-label="Card front">
    <div class="ghost-name" aria-hidden="true">VELMOR</div>
    <svg class="card__bg" viewBox="0 0 844 482" aria-hidden="true">
      <circle cx="164" cy="241" r="260" fill="var(--arc-3)"/>
      <circle cx="118" cy="241" r="259" fill="var(--arc-2)"/>
      <circle cx="70" cy="241" r="259" fill="var(--arc-1)"/>
    </svg>
    <h1 class="wordmark"><span>Velmor</span><span>Home</span><span>Design</span></h1>
  </section>

  <section class="card card--back" aria-label="Card back">
    <div class="ghost-name" aria-hidden="true">VELMOR</div>
    <svg class="card__bg" viewBox="0 0 844 482" aria-hidden="true">
      <circle cx="615" cy="241" r="254" fill="var(--arc-light)"/>
      <rect x="615" y="0" width="229" height="482" fill="var(--arc-light)"/>
      <circle cx="650" cy="241" r="257" fill="var(--arc-mid)"/>
      <rect x="650" y="0" width="194" height="482" fill="var(--arc-mid)"/>
      <circle cx="683" cy="241" r="261" fill="var(--black)"/>
      <rect x="683" y="0" width="161" height="482" fill="var(--black)"/>
    </svg>
    <p class="wordmark"><span>Velmor</span><span>Home</span><span>Design</span></p>

    <div class="contact">
      <h2 class="contact__name">Noel Bramwit</h2>
      <div class="contact__rule contact__rule--name"></div>
      <p class="contact__line" style="top:188px">2715 N Parkline Road, Ste 348</p>
      <p class="contact__line" style="top:218px">Larkdale, TX 79999</p>
      <div class="contact__divider" style="top:251px;width:183px"></div>
      <p class="contact__line" style="top:262px">(555) 555 0187</p>
      <div class="contact__divider" style="top:296px;width:181px"></div>
      <p class="contact__line" style="top:311px">nbramwit@velmordesign.example</p>
      <div class="contact__divider" style="top:348px;width:290px"></div>
      <p class="contact__line" style="top:361px">Website: velmordesign.example</p>
    </div>
  </section>

</main>
</body>
</html>
```